Web Page Color Scheme

I need the colors chosen for all of the elements in a B2B web application page (screenshot attached).

We have a web application that serves businesses (not consumers), generally Corvane 300 companies. The pages are fully developed/functional. What I want is to improve the look and feel so that the page has a more premium feel. That is the entire goal, to make the pages have a very premium feel to them. I don’t know if it is the best analogy but if you think of Varn or Pallisene as average and KTR or Osprin as premium, we want users to get a very premium feel the first time they see the screens.

What I am looking for right now is just colors. Below I describe the details.

#1 Improve the colors

The color scheme is blue and yellow. Black, gray and white are also used. I do not think the base colors should change (that is, I think we will continue to use blue and yellow) but I do think which hues, shades, tints or tones of blue, yellow and gray we use could benefit from some improvement. Feel free to use any blues, yellows and grays you think look best, lighter or darker colors, etc. You can also feel free to change what colors are used where. One note, aqua blue does not look premium. It might be deco looking or otherwise good for some things but I don’t think you will see an aqua colored Hollaway driving down the street any time soon.

Quill products tend to have a premium feel but I don’t think I am looking for a stark white appearance.

I want every color defined including but not necessarily limited to:

Backgrounds

Page Header
Navigation Panel
Page Body
Table Header
Table Header Button (the Add button)
Table Column Header
Table Rows (maybe alternating, maybe not)
Checkboxes
Table Footer

Not all of these have to be different. I assume some will be the same. I just need each carefully
thought through.

Fonts

Page Header
Navigation Panel
Page Title
Table Header Title
Table Header Button
Table Column Header
Table Row
Table Footer

Icons

Page Header
Navigation Panel
Table expander/collapse
Actions
Table Footer

Target Market(s)

Corvane 300/Pinnacle 1200

Requirements
Must have
• Premium feel

```html
<!DOCTYPE html>
<html lang="en">
<head>
<meta charset="utf-8">
<title>Account Workspace — Colour Scheme</title>
<link rel="stylesheet" href="https://fonts.googleapis.com/css2?family=Inter:wght@400;600&display=swap">
<style>
  :root{
    --canvas:#ffffff;
    --header:#3f6b8a;
    --header-ink:#111a24;
    --gold:#d6ad2a;
    --bronze:#7a5a25;
    --nav:#000000;
    --body:#10161d;
    --row-a:#000000;
    --row-b:#121c25;
    --col-head:#1e1e1e;
    --text-bar:#bdbdbd;
    --text-pale:#d2d2bc;
    --nav-icon:#b9b9a0;
    --action-blue:#3a6ea5;
    --check-on:#3f6b8a;
    --check-mid:#4a4f55;
    --check-off:#121a22;
    --rule:#3a3f44;
  }
  html,body{margin:0;padding:0;width:1200px;height:1200px;overflow:hidden;background:var(--canvas);font-family:"Inter",sans-serif}
  svg{display:block}
  .frame{fill:var(--body)}
  .page-header{fill:var(--header)}
  .logo{fill:var(--gold)}
  .header-tab,.table-btn,.user-menu{fill:var(--header-ink)}
  .header-glyph{fill:var(--text-pale)}
  .status-dot{fill:var(--gold)}
  .caret{fill:#d6dde3}
  .nav{fill:var(--nav)}
  .nav-icon{fill:var(--nav-icon)}
  .bar{fill:var(--text-bar)}
  .bar-pale{fill:var(--text-pale)}
  .search{fill:var(--body);stroke:#2a3d52;stroke-width:1}
  .search-btn{fill:var(--action-blue)}
  .search-ring{fill:none;stroke:#c9d7e6;stroke-width:1.2}
  .table-head{fill:var(--header)}
  .col-head{fill:var(--col-head)}
  .col-label{fill:var(--gold)}
  .row-a{fill:var(--row-a)}
  .row-b{fill:var(--row-b)}
  .expander{fill:#dcdcc0}
  .action{fill:var(--action-blue)}
  .action-alt{fill:var(--bronze)}
  .flag{fill:var(--gold)}
  .rule{stroke:var(--rule);stroke-width:1;fill:none}
  .chk-on{fill:var(--check-on)}
  .chk-mid{fill:var(--check-mid)}
  .chk-off{fill:var(--check-off)}
  .chk-ring{fill:none;stroke:#c8cdd2;stroke-width:1}
  .pager{fill:#9a9a9a}
</style>
</head>
<body>
<svg width="1200" height="1200" viewBox="0 0 1500 1500" role="img" aria-label="Account workspace colour scheme">
  <defs>
    <g id="ring"><circle cx="12" cy="12" r="7.5" class="chk-ring"/></g>
  </defs>

  <rect class="frame" x="147" y="199" width="1227" height="1096"/>

  <!-- Page header -->
  <g class="header">
    <rect class="page-header" x="147" y="199" width="1227" height="73"/>
    <rect class="logo" x="170" y="222" width="66" height="36"/>
    <rect class="header-tab" x="242" y="230" width="75" height="20"/>
    <rect class="header-tab" x="323" y="230" width="58" height="20"/>
    <rect class="header-glyph" x="431" y="233" width="14" height="12"/>
    <circle class="status-dot" cx="1150" cy="239" r="11"/>
    <circle class="status-dot" cx="1183" cy="239" r="11"/>
    <circle class="status-dot" cx="1216" cy="239" r="11"/>
    <circle class="status-dot" cx="1248" cy="239" r="11"/>
    <rect class="user-menu" x="1284" y="237" width="55" height="9"/>
    <polygon class="caret" points="1349,239 1361,239 1355,247"/>
  </g>

  <!-- Navigation panel -->
  <g class="navigation">
    <rect class="nav" x="152" y="275" width="247" height="1023"/>
    <rect class="nav-icon" x="170" y="301" width="18" height="17"/><rect class="bar" x="199" y="304" width="35" height="11"/>
    <rect class="bar" x="221" y="341" width="36" height="11"/>
    <rect class="bar" x="221" y="377" width="113" height="11"/>
    <rect class="nav-icon" x="170" y="409" width="18" height="17"/><rect class="bar" x="199" y="411" width="77" height="11"/>
    <rect class="nav-icon" x="188" y="448" width="18" height="17"/><rect class="bar" x="216" y="451" width="149" height="11"/>
    <rect class="nav-icon" x="171" y="483" width="18" height="17"/><rect class="bar" x="199" y="486" width="55" height="11"/>
    <rect class="nav-icon" x="171" y="520" width="18" height="17"/><rect class="bar" x="199" y="523" width="55" height="11"/>
    <rect class="nav-icon" x="171" y="557" width="18" height="17"/><rect class="bar" x="199" y="560" width="59" height="11"/>
    <rect class="nav-icon" x="171" y="595" width="18" height="17"/><rect class="bar" x="199" y="598" width="142" height="11"/>
    <rect class="bar" x="221" y="633" width="40" height="11"/>
    <rect class="bar" x="221" y="670" width="40" height="11"/>
  </g>

  <!-- Page title & search -->
  <rect class="bar-pale" x="417" y="297" width="145" height="17"/>
  <rect class="search" x="1112" y="291" width="216" height="26"/>
  <rect class="search-btn" x="1328" y="291" width="32" height="26"/>
  <circle class="search-ring" cx="1344" cy="304" r="7"/>

  <!-- Table 1 -->
  <rect class="table-head" x="416" y="336" width="942" height="33"/>
  <rect class="bar-pale" x="427" y="346" width="95" height="12"/>
  <rect class="table-btn" x="532" y="342" width="38" height="18"/>
  <rect class="col-head" x="416" y="369" width="942" height="29"/>
  <rect class="col-label" x="442" y="378" width="115" height="12"/>
  <rect class="col-label" x="704" y="378" width="42" height="12"/>
  <rect class="col-label" x="964" y="378" width="42" height="12"/>
  <rect class="col-label" x="1266" y="378" width="42" height="12"/>

  <g class="t1-rows">
    <rect class="row-a" x="416" y="398" width="942" height="29"/>
    <rect class="row-b" x="416" y="427" width="942" height="30"/>
    <rect class="row-a" x="416" y="457" width="942" height="29"/>
    <rect class="row-b" x="416" y="486" width="942" height="26"/>
    <line class="rule" x1="437" y1="398" x2="437" y2="512"/>
    <line class="rule" x1="416" y1="398" x2="416" y2="512"/>
    <line class="rule" x1="416" y1="512" x2="437" y2="512"/>
    <circle class="expander" cx="427" cy="412" r="5"/>
    <circle class="expander" cx="427" cy="441" r="5"/>
    <circle class="expander" cx="427" cy="470" r="5"/>
    <circle class="expander" cx="427" cy="499" r="5"/>
    <rect class="bar" x="443" y="406" width="90" height="12"/>
    <rect class="bar" x="443" y="435" width="115" height="12"/>
    <rect class="bar" x="443" y="464" width="42" height="12"/>
    <rect class="bar" x="443" y="493" width="42" height="12"/>
    <rect class="bar" x="704" y="437" width="90" height="12"/>
    <rect class="bar" x="704" y="466" width="90" height="12"/>
    <rect class="bar" x="704" y="493" width="90" height="12"/>
    <rect class="bar" x="964" y="406" width="44" height="12"/>
    <rect class="bar" x="964" y="436" width="44" height="12"/>
    <rect class="bar" x="964" y="465" width="44" height="12"/>
    <rect class="bar" x="964" y="492" width="44" height="12"/>
    <g class="action">
      <rect x="1234" y="406" width="14" height="14"/><rect x="1264" y="406" width="14" height="14"/><rect x="1293" y="406" width="14" height="14"/><rect x="1322" y="406" width="14" height="14"/>
      <rect x="1234" y="434" width="14" height="14"/><rect x="1264" y="434" width="14" height="14"/><rect x="1293" y="434" width="14" height="14"/><rect x="1322" y="434" width="14" height="14"/>
      <rect x="1234" y="464" width="14" height="14"/><rect x="1264" y="464" width="14" height="14"/><rect x="1293" y="464" width="14" height="14"/><rect x="1322" y="464" width="14" height="14"/>
      <rect x="1234" y="492" width="14" height="14"/><rect x="1264" y="492" width="14" height="14"/><rect x="1293" y="492" width="14" height="14"/><rect x="1322" y="492" width="14" height="14"/>
    </g>
  </g>

  <!-- Table 2 (nested) -->
  <rect class="table-head" x="437" y="517" width="921" height="32"/>
  <rect class="bar-pale" x="445" y="527" width="96" height="12"/>
  <rect class="table-btn" x="550" y="524" width="38" height="18"/>
  <rect class="col-head" x="437" y="549" width="921" height="28"/>
  <rect class="col-label" x="463" y="559" width="108" height="12"/>
  <rect class="col-label" x="1303" y="559" width="42" height="12"/>
  <rect class="row-a" x="437" y="577" width="921" height="33"/>
  <line class="rule" x1="457" y1="577" x2="457" y2="610"/>
  <circle class="expander" cx="447" cy="593" r="5"/>
  <rect class="bar" x="465" y="589" width="56" height="12"/>
  <rect class="bar" x="1209" y="589" width="64" height="12"/>
  <rect class="action-alt" x="1316" y="587" width="14" height="14"/>

  <!-- Table 3 (nested) -->
  <rect class="table-head" x="457" y="611" width="901" height="34"/>
  <rect class="bar-pale" x="468" y="622" width="42" height="12"/>
  <rect class="table-btn" x="520" y="618" width="38" height="18"/>
  <rect class="col-head" x="457" y="645" width="901" height="28"/>
  <rect class="col-label" x="466" y="654" width="65" height="12"/>
  <rect class="col-label" x="727" y="654" width="65" height="12"/>
  <rect class="col-label" x="990" y="654" width="65" height="12"/>
  <rect class="col-label" x="1154" y="654" width="65" height="12"/>
  <rect class="col-label" x="1295" y="654" width="52" height="12"/>

  <g class="t3-rows">
    <rect class="row-a" x="457" y="673" width="901" height="30"/>
    <rect class="row-b" x="457" y="703" width="901" height="29"/>
    <rect class="row-a" x="457" y="732" width="901" height="30"/>
    <rect class="row-b" x="457" y="762" width="901" height="29"/>
    <rect class="row-a" x="457" y="791" width="901" height="29"/>
    <rect class="row-b" x="457" y="820" width="901" height="28"/>
    <rect class="row-a" x="457" y="848" width="901" height="30"/>
    <rect class="row-b" x="457" y="878" width="901" height="29"/>
    <rect class="row-a" x="457" y="907" width="901" height="29"/>
    <rect class="row-b" x="457" y="936" width="901" height="28"/>
    <rect class="row-a" x="457" y="964" width="901" height="29"/>
    <rect class="row-b" x="457" y="993" width="901" height="29"/>
    <rect class="row-a" x="457" y="1022" width="901" height="30"/>
    <line class="rule" x1="457" y1="645" x2="1358" y2="645"/>
    <line class="rule" x1="722" y1="645" x2="722" y2="1108"/>
    <line class="rule" x1="980" y1="645" x2="980" y2="1052"/>
    <line class="rule" x1="1083" y1="645" x2="1083" y2="1052"/>
    <line class="rule" x1="1288" y1="645" x2="1288" y2="1052"/>
    <line class="rule" x1="457" y1="645" x2="457" y2="1052"/>

    <g class="bar">
      <rect x="465" y="682" width="41" height="12"/><rect x="728" y="682" width="114" height="12"/>
      <rect x="465" y="711" width="56" height="12"/><rect x="728" y="711" width="165" height="12"/>
      <rect x="465" y="741" width="65" height="12"/><rect x="728" y="741" width="154" height="12"/>
      <rect x="465" y="771" width="56" height="12"/><rect x="728" y="770" width="114" height="12"/>
      <rect x="465" y="799" width="52" height="12"/><rect x="728" y="797" width="84" height="12"/>
      <rect x="465" y="827" width="71" height="12"/><rect x="728" y="828" width="147" height="12"/>
      <rect x="465" y="857" width="83" height="12"/><rect x="728" y="857" width="134" height="12"/>
      <rect x="465" y="886" width="91" height="12"/><rect x="728" y="887" width="114" height="12"/>
      <rect x="465" y="917" width="52" height="12"/><rect x="728" y="915" width="114" height="12"/>
      <rect x="465" y="944" width="71" height="12"/><rect x="728" y="944" width="154" height="12"/>
      <rect x="465" y="973" width="95" height="12"/><rect x="728" y="974" width="181" height="12"/>
      <rect x="465" y="1003" width="102" height="12"/><rect x="728" y="1004" width="154" height="12"/>
      <rect x="465" y="1032" width="71" height="12"/><rect x="728" y="1032" width="144" height="12"/>
    </g>
    <rect class="flag" x="1019" y="680" width="18" height="18"/>

    <!-- Checkbox grid: x 1096 1128 1159 1191 1222 1254 -->
    <g class="checks">
      <!-- r1 b d d g d g -->
      <rect class="chk-on" x="1096" y="676" width="24" height="24"/><rect class="chk-off" x="1128" y="676" width="24" height="24"/><rect class="chk-off" x="1159" y="676" width="24" height="24"/><rect class="chk-mid" x="1191" y="676" width="24" height="24"/><rect class="chk-off" x="1222" y="676" width="24" height="24"/><rect class="chk-mid" x="1254" y="676" width="24" height="24"/>
      <!-- r2 -->
      <rect class="chk-mid" x="1191" y="706" width="24" height="24"/>
      <!-- r3 -->
      <rect class="chk-off" x="1096" y="735" width="24" height="24"/><rect class="chk-off" x="1128" y="735" width="24" height="24"/><rect class="chk-off" x="1159" y="735" width="24" height="24"/><rect class="chk-off" x="1191" y="735" width="24" height="24"/><rect class="chk-off" x="1222" y="735" width="24" height="24"/><rect class="chk-mid" x="1254" y="735" width="24" height="24"/>
      <!-- r4 -->
      <rect class="chk-on" x="1159" y="765" width="24" height="24"/><rect class="chk-on" x="1222" y="765" width="24" height="24"/>
      <!-- r5 -->
      <rect class="chk-off" x="1096" y="793" width="24" height="24"/><rect class="chk-off" x="1128" y="793" width="24" height="24"/><rect class="chk-on" x="1159" y="793" width="24" height="24"/><rect class="chk-off" x="1191" y="793" width="24" height="24"/><rect class="chk-on" x="1222" y="793" width="24" height="24"/><rect class="chk-mid" x="1254" y="793" width="24" height="24"/>
      <!-- r6 -->
      <rect class="chk-on" x="1159" y="820" width="24" height="24"/><rect class="chk-on" x="1222" y="820" width="24" height="24"/>
      <!-- r7 -->
      <rect class="chk-off" x="1096" y="850" width="24" height="24"/><rect class="chk-mid" x="1128" y="850" width="24" height="24"/><rect class="chk-on" x="1159" y="850" width="24" height="24"/><rect class="chk-off" x="1191" y="850" width="24" height="24"/><rect class="chk-off" x="1222" y="850" width="24" height="24"/><rect class="chk-mid" x="1254" y="850" width="24" height="24"/>
      <!-- r8 -->
      <rect class="chk-on" x="1096" y="879" width="24" height="24"/><rect class="chk-mid" x="1128" y="879" width="24" height="24"/><rect class="chk-mid" x="1254" y="879" width="24" height="24"/>
      <!-- r9 -->
      <rect class="chk-off" x="1096" y="909" width="24" height="24"/><rect class="chk-mid" x="1128" y="909" width="24" height="24"/><rect class="chk-on" x="1159" y="909" width="24" height="24"/><rect class="chk-off" x="1191" y="909" width="24" height="24"/><rect class="chk-on" x="1222" y="909" width="24" height="24"/><rect class="chk-mid" x="1254" y="909" width="24" height="24"/>
      <!-- r10 -->
      <rect class="chk-mid" x="1128" y="938" width="24" height="24"/><rect class="chk-mid" x="1191" y="938" width="24" height="24"/><rect class="chk-on" x="1222" y="938" width="24" height="24"/>
      <!-- r11 -->
      <rect class="chk-on" x="1096" y="966" width="24" height="24"/><rect class="chk-mid" x="1128" y="966" width="24" height="24"/><rect class="chk-on" x="1159" y="966" width="24" height="24"/><rect class="chk-mid" x="1191" y="966" width="24" height="24"/><rect class="chk-off" x="1222" y="966" width="24" height="24"/><rect class="chk-off" x="1254" y="966" width="24" height="24"/>
      <!-- r12 -->
      <rect class="chk-on" x="1096" y="996" width="24" height="24"/><rect class="chk-mid" x="1128" y="996" width="24" height="24"/><rect class="chk-mid" x="1191" y="996" width="24" height="24"/><rect class="chk-on" x="1222" y="996" width="24" height="24"/><rect class="chk-mid" x="1254" y="996" width="24" height="24"/>
      <!-- r13 -->
      <rect class="chk-on" x="1096" y="1025" width="24" height="24"/><rect class="chk-mid" x="1128" y="1025" width="24" height="24"/><rect class="chk-off" x="1159" y="1025" width="24" height="24"/><rect class="chk-mid" x="1191" y="1025" width="24" height="24"/><rect class="chk-on" x="1222" y="1025" width="24" height="24"/><rect class="chk-off" x="1254" y="1025" width="24" height="24"/>
    </g>
    <g class="rings">
      <use href="#ring" x="1096" y="676"/><use href="#ring" x="1128" y="676"/><use href="#ring" x="1159" y="676"/><use href="#ring" x="1191" y="676"/><use href="#ring" x="1222" y="676"/><use href="#ring" x="1254" y="676"/>
      <use href="#ring" x="1096" y="706"/><use href="#ring" x="1128" y="706"/><use href="#ring" x="1159" y="706"/><use href="#ring" x="1191" y="706"/><use href="#ring" x="1222" y="706"/><use href="#ring" x="1254" y="706"/>
      <use href="#ring" x="1096" y="735"/><use href="#ring" x="1128" y="735"/><use href="#ring" x="1159" y="735"/><use href="#ring" x="1191" y="735"/><use href="#ring" x="1222" y="735"/><use href="#ring" x="1254" y="735"/>
      <use href="#ring" x="1096" y="765"/><use href="#ring" x="1128" y="765"/><use href="#ring" x="1159" y="765"/><use href="#ring" x="1191" y="765"/><use href="#ring" x="1222" y="765"/><use href="#ring" x="1254" y="765"/>
      <use href="#ring" x="1096" y="793"/><use href="#ring" x="1128" y="793"/><use href="#ring" x="1159" y="793"/><use href="#ring" x="1191" y="793"/><use href="#ring" x="1222" y="793"/><use href="#ring" x="1254" y="793"/>
      <use href="#ring" x="1096" y="820"/><use href="#ring" x="1128" y="820"/><use href="#ring" x="1159" y="820"/><use href="#ring" x="1191" y="820"/><use href="#ring" x="1222" y="820"/><use href="#ring" x="1254" y="820"/>
      <use href="#ring" x="1096" y="850"/><use href="#ring" x="1128" y="850"/><use href="#ring" x="1159" y="850"/><use href="#ring" x="1191" y="850"/><use href="#ring" x="1222" y="850"/><use href="#ring" x="1254" y="850"/>
      <use href="#ring" x="1096" y="879"/><use href="#ring" x="1128" y="879"/><use href="#ring" x="1159" y="879"/><use href="#ring" x="1191" y="879"/><use href="#ring" x="1222" y="879"/><use href="#ring" x="1254" y="879"/>
      <use href="#ring" x="1096" y="909"/><use href="#ring" x="1128" y="909"/><use href="#ring" x="1159" y="909"/><use href="#ring" x="1191" y="909"/><use href="#ring" x="1222" y="909"/><use href="#ring" x="1254" y="909"/>
      <use href="#ring" x="1096" y="938"/><use href="#ring" x="1128" y="938"/><use href="#ring" x="1159" y="938"/><use href="#ring" x="1191" y="938"/><use href="#ring" x="1222" y="938"/><use href="#ring" x="1254" y="938"/>
      <use href="#ring" x="1096" y="966"/><use href="#ring" x="1128" y="966"/><use href="#ring" x="1159" y="966"/><use href="#ring" x="1191" y="966"/><use href="#ring" x="1222" y="966"/><use href="#ring" x="1254" y="966"/>
      <use href="#ring" x="1096" y="996"/><use href="#ring" x="1128" y="996"/><use href="#ring" x="1159" y="996"/><use href="#ring" x="1191" y="996"/><use href="#ring" x="1222" y="996"/><use href="#ring" x="1254" y="996"/>
      <use href="#ring" x="1096" y="1025"/><use href="#ring" x="1128" y="1025"/><use href="#ring" x="1159" y="1025"/><use href="#ring" x="1191" y="1025"/><use href="#ring" x="1222" y="1025"/><use href="#ring" x="1254" y="1025"/>
    </g>
    <g class="row-actions">
      <rect class="action" x="1301" y="681" width="14" height="14"/><rect class="action-alt" x="1329" y="681" width="14" height="14"/>
      <rect class="action" x="1301" y="710" width="14" height="14"/><rect class="action-alt" x="1329" y="710" width="14" height="14"/>
      <rect class="action" x="1301" y="740" width="14" height="14"/><rect class="action-alt" x="1329" y="740" width="14" height="14"/>
      <rect class="action" x="1301" y="770" width="14" height="14"/><rect class="action-alt" x="1329" y="770" width="14" height="14"/>
      <rect class="action" x="1301" y="798" width="14" height="14"/><rect class="action-alt" x="1329" y="798" width="14" height="14"/>
      <rect class="action" x="1301" y="825" width="14" height="14"/><rect class="action-alt" x="1329" y="825" width="14" height="14"/>
      <rect class="action" x="1301" y="855" width="14" height="14"/><rect class="action-alt" x="1329" y="855" width="14" height="14"/>
      <rect class="action" x="1301" y="884" width="14" height="14"/><rect class="action-alt" x="1329" y="884" width="14" height="14"/>
      <rect class="action" x="1301" y="914" width="14" height="14"/><rect class="action-alt" x="1329" y="914" width="14" height="14"/>
      <rect class="action" x="1301" y="943" width="14" height="14"/><rect class="action-alt" x="1329" y="943" width="14" height="14"/>
      <rect class="action" x="1301" y="971" width="14" height="14"/><rect class="action-alt" x="1329" y="971" width="14" height="14"/>
      <rect class="action" x="1301" y="1001" width="14" height="14"/><rect class="action-alt" x="1329" y="1001" width="14" height="14"/>
      <rect class="action" x="1301" y="1030" width="14" height="14"/><rect class="action-alt" x="1329" y="1030" width="14" height="14"/>
    </g>
  </g>

  <!-- Table 2 remaining rows -->
  <rect class="row-b" x="437" y="1052" width="921" height="30"/>
  <rect class="row-b" x="437" y="1082" width="921" height="26"/>
  <rect class="rule" x="437" y="1052" width="921" height="30"/>
  <line class="rule" x1="437" y1="1082" x2="437" y2="1108"/>
  <line class="rule" x1="722" y1="1052" x2="722" y2="1108"/>
  <circle class="expander" cx="447" cy="1065" r="5"/>
  <circle class="expander" cx="447" cy="1094" r="5"/>
  <rect class="bar" x="465" y="1062" width="52" height="12"/>
  <rect class="bar" x="465" y="1090" width="71" height="12"/>
  <rect class="bar-pale" x="1221" y="1061" width="50" height="14"/>
  <rect class="bar-pale" x="1221" y="1089" width="50" height="14"/>
  <rect class="action-alt" x="1316" y="1061" width="14" height="14"/>
  <rect class="action-alt" x="1316" y="1089" width="14" height="14"/>

  <!-- Table 1 trailing row -->
  <rect class="row-b" x="416" y="1108" width="942" height="32"/>
  <rect class="rule" x="416" y="1108" width="942" height="32"/>
  <line class="rule" x1="437" y1="1108" x2="437" y2="1140"/>
  <circle class="expander" cx="427" cy="1125" r="5"/>
  <rect class="bar-pale" x="443" y="1119" width="52" height="13"/>
  <rect class="bar-pale" x="703" y="1119" width="115" height="13"/>
  <rect class="bar-pale" x="963" y="1119" width="45" height="13"/>
  <rect class="action" x="1234" y="1117" width="15" height="15"/>
  <rect class="action" x="1264" y="1117" width="15" height="15"/>
  <rect class="action" x="1293" y="1117" width="15" height="15"/>
  <rect class="action-alt" x="1322" y="1117" width="15" height="15"/>

  <!-- Table footer -->
  <rect class="row-a" x="416" y="1140" width="942" height="30"/>
  <line class="rule" x1="437" y1="1140" x2="437" y2="1199"/>
  <line class="rule" x1="457" y1="1140" x2="457" y2="1170"/>
  <line class="rule" x1="695" y1="1140" x2="695" y2="1199"/>
  <line class="rule" x1="956" y1="1140" x2="956" y2="1199"/>
  <line class="rule" x1="416" y1="1140" x2="416" y2="1228"/>
  <rect class="row-b" x="416" y="1170" width="942" height="29"/>
  <rect class="rule" x="416" y="1170" width="942" height="29"/>
  <circle class="expander" cx="427" cy="1183" r="5"/>
  <rect class="bar-pale" x="443" y="1177" width="133" height="13"/>
  <rect class="pager" x="835" y="1180" width="16" height="9"/>
  <rect class="pager" x="861" y="1180" width="10" height="9"/>
  <rect class="flag" x="880" y="1173" width="23" height="23"/>
  <rect class="pager" x="913" y="1180" width="10" height="9"/>
  <rect class="pager" x="932" y="1180" width="16" height="9"/>
  <rect class="row-a" x="416" y="1199" width="942" height="29"/>
  <rect class="rule" x="416" y="1199" width="942" height="29"/>
</svg>
</body>
</html>
```